CAPABILITIES BROCHURE for an Engineering/Manufacturing Company
Ninebrook Power
CAPABILITIES BROCHURE for an Engineering/Manufacturing Company - Engineering
Creative Brief
Engineering
Corporate. Oil & Gas and Industrial Customers worldwide.
-A Front Cover and Back Cover -Even amount of pages and no more than 12, including front and back. -To stay on the same branding look we have been following and to incorporate the design of our folder since we will hand them out together. -Refer to our website for more information about Ninebrook, (this website is not complete so please take that into consideration) http://qlm.example-stage.net/ -To show a separation of sections. Like "Products" Section and "Who we are section". This way we can print them separately in the future as smaller hand outs. -Please design our Capabilities Chart, Timeline and "QUILLON" program to incorporate it into the brochure. Please design these with creativity. -Please message me if you have any questions whatsoever. I will be available US Central time from 8AM-MIDNIGHT (12AM) to answer any questions and to provide feedback.
fulllord fulllord
greetings, can i participate or you have already selected the winner thanks,and have good day
hjacobs hjacobs
Thank you again everyone. My bosses and I are finalizing designs. If I gave you one star, this means we are going in a different direction for the design. We appreciate everyone hard work. Please let me know if you have any questions.
Thank you everyone for your designs so far!! We are still waiting for a few more submissions. In the mean time I will be giving star ratings and providing a little bit of feedback. Please message me if you have any questions!!
SiteAdmin SiteAdmin
Designers, Please only use images provided by the project holder. If in case source of images has not been provided, you are requested to use images from “www.pixelmoorimages.example”. Images used from any other website or source will not be accepted. In case you are using images from “www.pixelmoorimages.example”, please make sure to keep a record of image ID numbers as contest winners will be required to provide those ID's. Furthermore, designers are requested only to use system fonts on all web design projects, files with non-system fonts will not be accepted. DESIGNERS ARE STRICTLY ADVISED TO ABIDE TO THESE RULES. STRICT ACTION WOULD BE TAKEN IN CASE OF ANY VIOLATION. Thanks! QR/TWK/HP/NV Team

```html
<!DOCTYPE html>
<html lang="en">
<head>
<meta charset="utf-8">
<title>Ninebrook Power – Capabilities Spread</title>
<link href="https://fonts.googleapis.com/css2?family=Source+Sans+3:ital,wght@0,400;0,600;0,700;1,400;1,600&display=swap" rel="stylesheet">
<style>
:root{
  --green:#73ad3f;
  --green-dark:#4f8a2a;
  --navy:#1d4a86;
  --blue:#2f6db5;
  --blue-light:#dce8f6;
  --orange:#f29a1f;
  --dot-green:#58b04a;
  --dot-blue:#2b7fd3;
  --ink:#3c3c3c;
  --rule:#c9d6e6;
  --paper:#ffffff;
}
*{box-sizing:border-box;margin:0;padding:0}
html,body{width:1200px;height:778px;overflow:hidden;background:var(--paper)}
body{font-family:"Source Sans 3",Arial,sans-serif;color:var(--ink)}
.spread{position:relative;width:1200px;height:778px;overflow:hidden}
.page{position:absolute;top:0;height:778px;width:600px;overflow:hidden}
.page-left{left:0}
.page-right{left:600px;background:linear-gradient(160deg,#ffffff 55%,#eef1f5 100%)}

/* left page */
.solar-photo{position:absolute;left:0;top:0;width:600px;height:218px;
  background:linear-gradient(135deg,#9cc3e6 0%,#3b6ea8 40%,#1d3f6b 75%,#5a87b8 100%)}
.renewable{position:absolute;left:22px;top:224px;width:560px}
.renewable h2{font-size:25px;font-weight:600;color:#4a4a4a;letter-spacing:-.2px}
.renewable h2 strong{color:var(--green);font-weight:700}
.renewable .cols{display:flex;gap:16px;margin-top:6px}
.renewable p{flex:1;font-size:9.4px;line-height:1.36;color:#555}
.sky-photo{position:absolute;left:0;top:372px;width:228px;height:406px;
  background:linear-gradient(180deg,#cfe3f5 0%,#8fbbe3 45%,#5b8fc3 100%)}
.facility{position:absolute;left:228px;top:372px;width:372px;height:406px;
  background:linear-gradient(160deg,var(--green) 0%,var(--green-dark) 100%);
  color:#fff;padding:80px 22px 0 26px}
.facility h3{font-weight:600;line-height:1.12}
.facility .listed{font-size:22px}
.facility .cert{font-size:27px;font-weight:700}
.facility .place{font-size:27px;font-weight:700}
.facility p{font-size:9.2px;line-height:1.38;margin-top:10px;opacity:.95}

/* right page */
.swoosh{position:absolute;left:0;top:0;width:600px;height:778px}
.section-title{position:absolute;left:20px;width:580px;height:36px;
  background:linear-gradient(90deg,#ffffff 0%,var(--blue-light) 35%,#b9d0ec 100%);
  color:var(--navy);font-size:21px;font-weight:600;text-align:right;padding:4px 14px 0 0}
.title-products{top:53px}
.title-services{top:425px}
.cap-table{position:absolute;left:20px;width:572px;border-collapse:collapse;table-layout:fixed}
.cap-products{top:95px}
.cap-services{top:465px}
.cap-table th{background:var(--blue);color:#fff;font-size:8px;font-weight:600;height:17px;
  border-left:1px solid #fff}
.cap-table th:first-child{border-left:0}
.cap-table td{font-size:8.6px;line-height:1.1;border-bottom:1px solid var(--rule);
  border-left:1px solid var(--rule);text-align:center;height:17px;padding:0 4px}
.cap-table td:first-child{text-align:left;border-left:0;color:#333}
.cap-table tr.tall td{height:25px}
.cap-table col.name{width:196px}
.dot{display:inline-block;width:8px;height:8px;border-radius:50%;vertical-align:middle}
.o{background:var(--orange)}
.g{background:var(--dot-green)}
.b{background:var(--dot-blue)}
.footer-band{position:absolute;left:20px;top:736px;width:580px;height:28px;
  background:linear-gradient(90deg,var(--blue-light) 0%,var(--blue) 45%,var(--navy) 100%);
  display:flex;align-items:center;justify-content:space-between;padding:0 14px 0 12px;color:#fff}
.footer-band .claim{font-style:italic;font-size:12px;color:var(--navy);font-weight:600}
.footer-band .web{display:flex;align-items:center;gap:6px;font-size:13px;font-weight:600}
</style>
</head>
<body>
<div class="spread">

  <section class="page page-left">
    <div class="solar-photo" role="img" aria-label="Photo collage of solar panel arrays under a blue sky"></div>

    <div class="renewable">
      <h2>Renewable Energy <strong>Solutions</strong></h2>
      <div class="cols">
        <p>Ninebrook Power provides control panels, monitoring and modules for most renewable energy markets including the Solar &amp; Wind Industry. Our vast experience with the design and packaging of variable frequency drives permitted an easy entry into the renewable market. We can provide packaged Inverter solutions required to convert DC power to AC power for interface with transmission lines or substations.</p>
        <p>Extreme climate conditions along with innovative packaging allow higher reliability and system integrity. State of the art energy monitoring technology can be utilized to view panel level efficiencies throughout the solar array and farm and compare those values to the same panel or array over user selected time periods. Maintenance and service are available for all our renewable products.</p>
      </div>
    </div>

    <div class="sky-photo" role="img" aria-label="Photo of power lines and wind turbines against a blue sky"></div>

    <div class="facility">
      <h3 class="listed">UL 508 and UL698A Listed</h3>
      <h3 class="cert">ISO 9001 Certified</h3>
      <h3 class="place">Controls Facility</h3>
      <p>Ninebrook Power designs and manufactures UL 508 Listed Control Panels for all industries including Municipal, Industrial, Oil &amp; Gas, Commercial and Irrigation applications. Ninebrook is certified to build UL 698A intrinsically safe control panels for process control in extreme hazardous locations. Our team is comprised of highly qualified and experienced members who are dedicated to exceeding our customer's needs and future expectations. As an independent manufacturer we have the flexibility to choose from a variety of suppliers which allows us to fulfill our customer's unique requirements.</p>
      <p>The best selection is often driven by specifications, end-user customer preference, or the need to be competitive without compromising quality. All of our products are certified and manufactured according to the ISO 9001 standards for quality management.</p>
    </div>
  </section>

  <section class="page page-right">
    <svg class="swoosh" viewBox="0 0 600 778" aria-hidden="true">
      <path d="M0 600 C160 520 340 700 600 560 L600 778 L0 778 Z" fill="#eef2f7"/>
      <path d="M0 660 C200 590 380 760 600 640" fill="none" stroke="#e2e8f0" stroke-width="6"/>
    </svg>

    <h2 class="section-title title-products">Ninebrook Power Product &amp; Service Capabilities</h2>
    <table class="cap-table cap-products">
      <colgroup><col class="name"><col><col><col><col><col><col><col><col></colgroup>
      <thead><tr><th>PRODUCTS</th><th>120-240V</th><th>480-690V</th><th>2300V</th><th>3300V</th><th>4160V</th><th>7200V</th><th>10/11,000V</th><th>13200V</th></tr></thead>
      <tbody>
        <tr class="tall"><td>Medium Voltage Variable Frequency Drive</td><td></td><td></td><td><i class="dot g"></i></td><td><i class="dot g"></i></td><td><i class="dot b"></i></td><td><i class="dot g"></i></td><td><i class="dot b"></i></td><td><i class="dot g"></i></td></tr>
        <tr><td>Medium voltage Solid State Starters</td><td></td><td></td><td><i class="dot g"></i></td><td><i class="dot g"></i></td><td><i class="dot b"></i></td><td><i class="dot g"></i></td><td><i class="dot b"></i></td><td><i class="dot g"></i></td></tr>
        <tr><td>Medium Voltage Integrated Systems</td><td></td><td></td><td><i class="dot g"></i></td><td><i class="dot g"></i></td><td><i class="dot b"></i></td><td><i class="dot g"></i></td><td><i class="dot b"></i></td><td><i class="dot g"></i></td></tr>
        <tr><td>Medium Voltage Synch Bypass Systems</td><td></td><td></td><td><i class="dot g"></i></td><td><i class="dot g"></i></td><td><i class="dot b"></i></td><td><i class="dot g"></i></td><td><i class="dot b"></i></td><td><i class="dot g"></i></td></tr>
        <tr><td>Medium voltage Static Var Systems</td><td></td><td></td><td><i class="dot g"></i></td><td><i class="dot g"></i></td><td><i class="dot b"></i></td><td><i class="dot g"></i></td><td><i class="dot b"></i></td><td><i class="dot g"></i></td></tr>
        <tr><td>Power Control Rooms</td><td></td><td></td><td><i class="dot g"></i></td><td><i class="dot g"></i></td><td><i class="dot b"></i></td><td><i class="dot g"></i></td><td><i class="dot b"></i></td><td><i class="dot g"></i></td></tr>
        <tr><td>Circuit Breaker and Disconnects</td><td><i class="dot o"></i></td><td><i class="dot o"></i></td><td><i class="dot g"></i></td><td><i class="dot g"></i></td><td><i class="dot b"></i></td><td><i class="dot g"></i></td><td><i class="dot b"></i></td><td><i class="dot g"></i></td></tr>
        <tr class="tall"><td>Direct on Line and ATL Starters and Controls</td><td><i class="dot o"></i></td><td><i class="dot o"></i></td><td><i class="dot g"></i></td><td><i class="dot g"></i></td><td><i class="dot b"></i></td><td><i class="dot g"></i></td><td><i class="dot b"></i></td><td><i class="dot g"></i></td></tr>
        <tr><td>Electric AC &amp; DC Motors</td><td><i class="dot o"></i></td><td><i class="dot o"></i></td><td><i class="dot g"></i></td><td><i class="dot g"></i></td><td><i class="dot b"></i></td><td><i class="dot g"></i></td><td><i class="dot b"></i></td><td><i class="dot g"></i></td></tr>
        <tr><td>Automation Systems</td><td><i class="dot o"></i></td><td><i class="dot o"></i></td><td><i class="dot g"></i></td><td><i class="dot g"></i></td><td><i class="dot b"></i></td><td><i class="dot g"></i></td><td><i class="dot b"></i></td><td><i class="dot g"></i></td></tr>
        <tr><td>DCS/SCADA/PLC Systems</td><td><i class="dot o"></i></td><td><i class="dot o"></i></td><td><i class="dot g"></i></td><td><i class="dot g"></i></td><td><i class="dot b"></i></td><td><i class="dot g"></i></td><td><i class="dot b"></i></td><td><i class="dot g"></i></td></tr>
        <tr class="tall"><td>Complete Engineered Integrated Solutions</td><td><i class="dot o"></i></td><td><i class="dot o"></i></td><td><i class="dot g"></i></td><td><i class="dot g"></i></td><td><i class="dot b"></i></td><td><i class="dot g"></i></td><td><i class="dot b"></i></td><td><i class="dot g"></i></td></tr>
        <tr><td>Low Voltage Solid State Starters</td><td><i class="dot o"></i></td><td><i class="dot o"></i></td><td></td><td></td><td></td><td></td><td></td><td></td></tr>
        <tr><td>Low Voltage Variable Frequency Drives</td><td><i class="dot o"></i></td><td><i class="dot o"></i></td><td></td><td></td><td></td><td></td><td></td><td></td></tr>
        <tr><td>Low Voltage Motor Controls</td><td><i class="dot o"></i></td><td><i class="dot o"></i></td><td></td><td></td><td></td><td></td><td></td><td></td></tr>
      </tbody>
    </table>

    <h2 class="section-title title-services">Technical &amp; Engineering Services</h2>
    <table class="cap-table cap-services">
      <colgroup><col class="name"><col><col><col><col><col><col><col><col></colgroup>
      <thead><tr><th>PRODUCTS</th><th>120-240V</th><th>480-690V</th><th>2300V</th><th>3300V</th><th>4160V</th><th>7200V</th><th>10/11,000V</th><th>13200V</th></tr></thead>
      <tbody>
        <tr class="tall"><td>Service &amp; Repair of AC &amp; DC Motor Controls</td><td><i class="dot o"></i></td><td><i class="dot o"></i></td><td><i class="dot g"></i></td><td><i class="dot g"></i></td><td><i class="dot b"></i></td><td><i class="dot g"></i></td><td><i class="dot b"></i></td><td><i class="dot g"></i></td></tr>
        <tr><td>Diagnostics &amp; Troubleshooting</td><td><i class="dot o"></i></td><td><i class="dot o"></i></td><td><i class="dot g"></i></td><td><i class="dot g"></i></td><td><i class="dot b"></i></td><td><i class="dot g"></i></td><td><i class="dot b"></i></td><td><i class="dot g"></i></td></tr>
        <tr><td>System Retrofit &amp; Replacements</td><td><i class="dot o"></i></td><td><i class="dot o"></i></td><td><i class="dot g"></i></td><td><i class="dot g"></i></td><td><i class="dot b"></i></td><td><i class="dot g"></i></td><td><i class="dot b"></i></td><td><i class="dot g"></i></td></tr>
        <tr><td>Commissioning &amp; Installation Services</td><td><i class="dot o"></i></td><td><i class="dot o"></i></td><td><i class="dot g"></i></td><td><i class="dot g"></i></td><td><i class="dot b"></i></td><td><i class="dot g"></i></td><td><i class="dot b"></i></td><td><i class="dot g"></i></td></tr>
        <tr><td>Product Evaluation &amp; Repair</td><td><i class="dot o"></i></td><td><i class="dot o"></i></td><td><i class="dot g"></i></td><td><i class="dot g"></i></td><td><i class="dot b"></i></td><td><i class="dot g"></i></td><td><i class="dot b"></i></td><td><i class="dot g"></i></td></tr>
        <tr><td>Technical Phone Support</td><td><i class="dot o"></i></td><td><i class="dot o"></i></td><td><i class="dot g"></i></td><td><i class="dot g"></i></td><td><i class="dot b"></i></td><td><i class="dot g"></i></td><td><i class="dot b"></i></td><td><i class="dot g"></i></td></tr>
        <tr><td>Preventative Maintenance Contracts</td><td><i class="dot o"></i></td><td><i class="dot o"></i></td><td><i class="dot g"></i></td><td><i class="dot g"></i></td><td><i class="dot b"></i></td><td><i class="dot g"></i></td><td><i class="dot b"></i></td><td><i class="dot g"></i></td></tr>
        <tr class="tall"><td>ICAD/SCADA/DCS System Evaluation &amp; Improvement</td><td><i class="dot o"></i></td><td><i class="dot o"></i></td><td><i class="dot g"></i></td><td><i class="dot g"></i></td><td><i class="dot b"></i></td><td><i class="dot g"></i></td><td><i class="dot b"></i></td><td><i class="dot g"></i></td></tr>
        <tr><td>PLC System Design &amp; Programming</td><td><i class="dot o"></i></td><td><i class="dot o"></i></td><td><i class="dot g"></i></td><td><i class="dot g"></i></td><td><i class="dot b"></i></td><td><i class="dot g"></i></td><td><i class="dot b"></i></td><td><i class="dot g"></i></td></tr>
        <tr><td>Power Quality Analysis Services</td><td><i class="dot o"></i></td><td><i class="dot o"></i></td><td><i class="dot g"></i></td><td><i class="dot g"></i></td><td><i class="dot b"></i></td><td><i class="dot g"></i></td><td><i class="dot b"></i></td><td><i class="dot g"></i></td></tr>
        <tr><td>Harmonic Testing</td><td><i class="dot o"></i></td><td><i class="dot o"></i></td><td><i class="dot g"></i></td><td><i class="dot g"></i></td><td><i class="dot b"></i></td><td><i class="dot g"></i></td><td><i class="dot b"></i></td><td><i class="dot g"></i></td></tr>
        <tr><td>Training</td><td><i class="dot o"></i></td><td><i class="dot o"></i></td><td><i class="dot g"></i></td><td><i class="dot g"></i></td><td><i class="dot b"></i></td><td><i class="dot g"></i></td><td><i class="dot b"></i></td><td><i class="dot g"></i></td></tr>
      </tbody>
    </table>

    <div class="footer-band">
      <span class="claim">"ISO 9001 Certified Quality Management System".</span>
      <span class="web">
        <svg width="14" height="14" viewBox="0 0 14 14" aria-hidden="true"><circle cx="7" cy="7" r="6" fill="none" stroke="#fff" stroke-width="1.3"/><ellipse cx="7" cy="7" rx="2.6" ry="6" fill="none" stroke="#fff" stroke-width="1"/><line x1="1" y1="7" x2="13" y2="7" stroke="#fff" stroke-width="1"/></svg>
        www.qlm.example
      </span>
    </div>
  </section>

</div>
</body>
</html>
```